ZoVEX App logo & homescreen design

We are creating a new app call "ZoVEX" that is designed for young adults (15-24 years old) to create a sexual risk reduction plan to help young adults follow their relationship goals while also being safe. Currently, we need graphic design for the ZoVEX: (1) app logo and (2) a home screen for the app. We would like to see designs that are appealing to the target population - young adults ages 15-24. These requests are only the beginning of a series of graphic designs needs that I have to develop the app - and will offer one-on-one graphic design opportunities (much more $$$ to come) for the right graphic designer. The ZoVEX app is complimentary follow-up to another commercial app we have call KALDRO, designed for doctors to assess young adults' level of sexual risk during a dr. appointment (see vantrolibsoft.com for more details) after leaving a doctors visit. I have uploaded our company branding guidelines, but am open to any colors, fonts that are appealing to the target population.

Target Market(s)

youth 15-24 years of age

Industry/Entity Type

Health And Wellness

Colors

Designer to choose colors to be used in the design.

Requirements
Must have
• Both MUST be appealing to the target market.
• The app logo should be an icon or image that represents a plan.
• The homescreen UI needs to be easy to navigate and include 4 key sections: (1) Info - this section will include educational information tailored to their sexual risk level, (2) Plan - this section will link them to create their sexual risk reduction plan, (3) Sharing - this section will link them to areas that allow them to share their plan with their doctor or others, and (4) tip - this section may be a link OR the main part of the homescreen that shares daily/weekly tips on how to stick to their plan. I suggest getting inspiration from https://www.brindelfolio.com/30-recent-inspirational-ui-examples-in-mobile-device-screens.html.
Nice to have
• In app design focus groups, youth in the target market suggested that it would should have a similar look and feel to fizzlor because they LOVE that app.
Should not have
• imply its a sexual related or healthcare/wellness related - want to to seem fun & easy to use. I open to any ideas here and am looking for YOU to be CREATIVE!!!

```html
<!DOCTYPE html>
<html lang="en">
<head>
<meta charset="utf-8">
<title>ZoVEX – My Plan</title>
<link rel="stylesheet" href="https://fonts.googleapis.com/css2?family=Montserrat:wght@400;500;600&display=swap">
<style>
  :root {
    --screen-bg: #f9fafc;
    --card-bg: #ffffff;
    --ink: #2b3a5c;
    --muted: #8c96a8;
    --info-blue: #1fb3d6;
    --share-blue: #7fd4f2;
    --accent-red: #ef5a3c;
    --clip-orange: #f3a531;
    --clip-paper: #fdf3dc;
    --star-pink: #e6367f;
    --star-violet: #7b4fd6;
    --star-cyan: #29c2e0;
    --star-green: #34c46a;
    --star-yellow: #f7c531;
  }
  * { margin: 0; padding: 0; box-sizing: border-box; }
  html, body { width: 787px; height: 1200px; overflow: hidden; }
  body {
    background: var(--screen-bg);
    font-family: "Montserrat", sans-serif;
    color: var(--ink);
    position: relative;
  }
  .status-bar {
    position: absolute; top: 10px; left: 24px; right: 24px; height: 30px;
    display: flex; align-items: center; justify-content: space-between;
    font-size: 21px; font-weight: 500;
  }
  .status-left, .status-right { display: flex; align-items: center; gap: 8px; width: 240px; }
  .status-right { justify-content: flex-end; }
  .signal { display: flex; gap: 3px; }
  .signal span { width: 9px; height: 9px; border-radius: 50%; background: var(--ink); }
  .signal span.off { background: none; border: 1.5px solid var(--ink); }
  .battery { width: 46px; height: 18px; border: 2px solid var(--ink); border-radius: 3px; padding: 2px; position: relative; }
  .battery::after { content: ""; position: absolute; right: -5px; top: 4px; width: 3px; height: 6px; background: var(--ink); border-radius: 0 2px 2px 0; }
  .battery i { display: block; width: 100%; height: 100%; background: var(--ink); }
  .app-header {
    position: absolute; top: 58px; left: 0; right: 0; height: 56px;
    display: flex; align-items: center; justify-content: center;
  }
  .menu-toggle { position: absolute; left: 76px; top: 16px; width: 34px; display: flex; flex-direction: column; gap: 9px; }
  .menu-toggle span { height: 2.5px; background: var(--ink); border-radius: 2px; }
  .app-title { font-size: 32px; font-weight: 500; letter-spacing: 0.2px; }
  .card-grid {
    position: absolute; top: 198px; left: 33px;
    display: grid; grid-template-columns: 342px 342px; grid-template-rows: 387px 387px;
    column-gap: 36px; row-gap: 31px;
  }
  .section-card {
    background: var(--card-bg);
    box-shadow: 0 2px 10px rgba(43, 58, 92, 0.05);
    display: flex; flex-direction: column; align-items: center;
    padding-top: 84px; text-align: center;
  }
  .section-icon { width: 92px; height: 92px; }
  .illustration-slot { width: 80px; height: 92px; border-radius: 6px; }
  .illustration-slot.plan { background: linear-gradient(160deg, var(--clip-paper), var(--clip-orange)); }
  .illustration-slot.tips {
    width: 90px; height: 90px; border-radius: 50%;
    background: conic-gradient(var(--star-pink), var(--star-violet), var(--star-cyan), var(--star-green), var(--star-yellow), var(--star-pink));
    opacity: 0.85;
  }
  .section-title { margin-top: 30px; font-size: 28px; font-weight: 500; }
  .section-desc { margin-top: 12px; font-size: 15px; line-height: 20px; color: var(--muted); }
</style>
</head>
<body>
  <div class="status-bar">
    <div class="status-left">
      <div class="signal"><span></span><span></span><span></span><span class="off"></span><span class="off"></span></div>
      <span>VELTA</span>
      <svg width="22" height="18" viewBox="0 0 22 18" aria-hidden="true">
        <path d="M1 6a15 15 0 0 1 20 0M4.5 9.5a10 10 0 0 1 13 0M8 13a5 5 0 0 1 6 0" fill="none" stroke="#2b3a5c" stroke-width="2.4" stroke-linecap="round"/>
        <circle cx="11" cy="16" r="1.8" fill="#2b3a5c"/>
      </svg>
    </div>
    <span class="status-time">4:21 PM</span>
    <div class="status-right">
      <svg width="12" height="22" viewBox="0 0 12 22" aria-hidden="true">
        <path d="M1 6l10 10-5 5V1l5 5L1 16" fill="none" stroke="#8c96a8" stroke-width="1.6"/>
      </svg>
      <span>100%</span>
      <div class="battery"><i></i></div>
    </div>
  </div>

  <header class="app-header">
    <div class="menu-toggle" aria-label="Menu"><span></span><span></span><span></span></div>
    <h1 class="app-title">My Plan</h1>
  </header>

  <main class="card-grid">
    <section class="section-card">
      <svg class="section-icon" viewBox="0 0 92 92" aria-hidden="true">
        <circle cx="46" cy="46" r="46" fill="var(--info-blue)"/>
        <circle cx="51" cy="24" r="6" fill="#fff"/>
        <path d="M38 40h14l-6 28c-.5 3 2 3 6 0" fill="none" stroke="#fff" stroke-width="8" stroke-linecap="round" stroke-linejoin="round"/>
      </svg>
      <h2 class="section-title">Information</h2>
      <p class="section-desc">Educational Information<br>About Sexual Risks</p>
    </section>

    <section class="section-card">
      <div class="illustration-slot plan" role="img" aria-label="Illustration of a clipboard with a chart and a pencil"></div>
      <h2 class="section-title">Plan</h2>
      <p class="section-desc">Create Your Risk<br>Reduction Plan</p>
    </section>

    <section class="section-card">
      <svg class="section-icon" viewBox="0 0 92 92" aria-hidden="true">
        <circle cx="46" cy="46" r="46" fill="var(--share-blue)"/>
        <path d="M28 46L60 28M28 46l32 18" stroke="#2b3a5c" stroke-width="2.5"/>
        <circle cx="28" cy="46" r="8" fill="var(--accent-red)" stroke="#fff" stroke-width="3"/>
        <circle cx="60" cy="28" r="8" fill="#fff"/>
        <circle cx="60" cy="64" r="8" fill="#fff"/>
      </svg>
      <h2 class="section-title">Share</h2>
      <p class="section-desc">Share Plan With<br>Your Friends &amp; Doctors</p>
    </section>

    <section class="section-card">
      <div class="illustration-slot tips" role="img" aria-label="Illustration of a faceted rainbow star"></div>
      <h2 class="section-title">Tips</h2>
      <p class="section-desc">Create Your Risk<br>Reduction Plan</p>
    </section>
  </main>
</body>
</html>
```